Updated DJ business Card showing other businesses

DJ Kestro offers professional mobile dj services including DJ. MC. Karaoke.
Quietbeat Disco (will attach logo)
I also offer a 360 Photo Booth.

Contact info:
(555) 013-4472
marcus.tellgren@lumomail.net
Social Media @DJKestroNWX

```html
<!DOCTYPE html>
<html lang="en">
<head>
<meta charset="utf-8">
<title>DJ Kestro – Business Card</title>
<link href="https://fonts.googleapis.com/css2?family=Share+Tech+Mono&display=swap" rel="stylesheet">
<style>
  :root {
    --backdrop: #8c8797;
    --card-dark: #343434;
    --card-light: #ffffff;
    --ink-light: #ffffff;
    --ink-soft: #cfcfcf;
    --ink-dark: #161616;
    --accent: #d61a4a;
  }
  html, body {
    margin: 0;
    padding: 0;
    width: 1200px;
    height: 1200px;
    overflow: hidden;
    background: var(--backdrop);
    font-family: "Share Tech Mono", monospace;
  }
  .canvas {
    position: relative;
    width: 1200px;
    height: 1200px;
  }
  .card {
    position: absolute;
    width: 705px;
    height: 402px;
    box-shadow: 8px 10px 18px rgba(0, 0, 0, 0.35);
    overflow: hidden;
  }
  .card--front {
    left: 109px;
    top: 157px;
    background: var(--card-dark);
  }
  .card--back {
    left: 361px;
    top: 615px;
    background: var(--card-dark);
  }
  .card__wave {
    position: absolute;
    inset: 0;
    width: 100%;
    height: 100%;
  }
  .card__wave path { fill: var(--card-light); }

  .brand-lockup {
    position: absolute;
    display: flex;
    flex-direction: column;
    align-items: center;
  }
  .brand-lockup--front {
    left: 0;
    right: 0;
    top: 104px;
  }
  .brand-lockup--back {
    right: 46px;
    top: 240px;
    align-items: flex-end;
  }
  .partner-mark {
    display: flex;
    align-items: center;
    gap: 8px;
    font-size: 20px;
    letter-spacing: 1px;
    text-transform: uppercase;
  }
  .partner-mark__dot {
    width: 18px;
    height: 18px;
    border-radius: 50%;
    background: currentColor;
  }
  .brand-name {
    display: flex;
    align-items: center;
    gap: 14px;
    line-height: 1;
    text-transform: uppercase;
  }
  .brand-name__dot {
    border-radius: 50%;
    background: var(--accent);
  }
  .brand-lockup--front .partner-mark { color: var(--ink-light); margin-left: 90px; }
  .brand-lockup--front .brand-name { color: var(--ink-light); font-size: 92px; margin-top: 14px; }
  .brand-lockup--front .brand-name__dot { width: 46px; height: 46px; }
  .brand-lockup--back .partner-mark { color: var(--ink-dark); font-size: 15px; }
  .brand-lockup--back .partner-mark__dot { width: 14px; height: 14px; }
  .brand-lockup--back .brand-name { color: var(--ink-dark); font-size: 46px; margin-top: 10px; gap: 8px; }
  .brand-lockup--back .brand-name__dot { width: 24px; height: 24px; }

  .service-list {
    position: absolute;
    left: 0;
    right: 0;
    top: 300px;
    margin: 0;
    padding: 0;
    list-style: none;
    display: flex;
    justify-content: center;
    gap: 22px;
    color: var(--ink-soft);
    font-size: 19px;
    letter-spacing: 2px;
    text-transform: uppercase;
  }
  .service-list li + li::before {
    content: "";
    display: inline-block;
    width: 6px;
    height: 6px;
    margin: 0 22px 3px 0;
    border-radius: 50%;
    background: var(--accent);
  }

  .contact-list {
    position: absolute;
    left: 43px;
    top: 44px;
    margin: 0;
    padding: 0;
    list-style: none;
    color: var(--ink-light);
    font-size: 27px;
    text-transform: uppercase;
  }
  .contact-list li { height: 62px; }
</style>
</head>
<body>
<main class="canvas">
  <section class="card card--front" aria-label="Business card front">
    <div class="brand-lockup brand-lockup--front">
      <div class="partner-mark"><span class="partner-mark__dot"></span>Quietbeat Disco</div>
      <div class="brand-name"><span class="brand-name__dot"></span>DJ Kestro</div>
    </div>
    <ul class="service-list" aria-label="Services">
      <li>DJ</li>
      <li>MC</li>
      <li>Karaoke</li>
      <li>360 Photo Booth</li>
    </ul>
  </section>

  <section class="card card--back" aria-label="Business card back">
    <svg class="card__wave" viewBox="0 0 705 402" preserveAspectRatio="none" aria-hidden="true">
      <path d="M0,402 C130,270 270,225 440,205 C570,188 650,120 705,0 L705,402 Z"/>
    </svg>
    <ul class="contact-list">
      <li>(555) 013-4472</li>
      <li>marcus.tellgren@lumomail.net</li>
      <li>@DJKestroNWX</li>
    </ul>
    <div class="brand-lockup brand-lockup--back">
      <div class="partner-mark"><span class="partner-mark__dot"></span>Quietbeat Disco</div>
      <div class="brand-name"><span class="brand-name__dot"></span>DJ Kestro</div>
    </div>
  </section>
</main>
</body>
</html>
```